T-tariffs by VALMOND

Our new site consists of: - Publish a regulatory watch by allowing access to the latest regulations and news specific to its field of activity. It will be asked when registering to choose 2 areas of activity from a predefined list - Make available the customs documents (DAU) and reverse charge reports - Establishment of a personal space project on which we bring our customs expertise to the client in order to change the management of its flows, this space will also allow him to keep his authorizations, RTC etc - Exhibit statistical tools (graph, curves ...) from the customs documents loaded on the site Our targets are our current customers, our prospects (importers, exporters) There will therefore be a personal secure access to create. The colors and tones must remain on the logo. "Logical" contrasts are appreciated.

Target Market(s)

importer / exporters

Font styles to use
Serif
Sans Serif

Colors

Designer to choose colors to be used in the design.

Requirements
Must have
• the following topics: - regulatory watch (modern newspaper template) - pdf file release (summary)
Nice to have
• a modern and functional design

```html
<!DOCTYPE html>
<html lang="en">
<head>
<meta charset="utf-8">
<title>T-tariffs by VALMOND</title>
<link href="https://fonts.googleapis.com/css2?family=Lato:wght@400;700;900&display=swap" rel="stylesheet">
<style>
:root{
  --red:#e84a1f;
  --blue:#1f97dd;
  --blue-dark:#1a8bcf;
  --date:#2a8fd4;
  --ink:#1f1f1f;
  --muted:#6b6b6b;
  --line:#dcdcdc;
  --panel-head:#e8e8e8;
  --white:#fff;
}
*{box-sizing:border-box;margin:0;padding:0}
html,body{width:1200px;height:2409px;overflow:hidden}
body{position:relative;background:var(--white);font-family:'Lato',sans-serif;color:var(--ink)}
.abs{position:absolute}
a{color:inherit;text-decoration:none}

/* header */
.site-header{position:absolute;left:0;top:0;width:1200px;height:85px;background:var(--white)}
.brand{position:absolute;left:144px;top:18px;display:flex;align-items:center;gap:8px;color:var(--blue);font-weight:900;font-size:28px;letter-spacing:.5px}
.brand .dot{width:14px;height:14px;background:var(--red)}
.brand small{font-size:14px;font-weight:900;color:var(--blue);align-self:flex-end;margin-bottom:3px}
.main-nav{position:absolute;left:474px;top:35px;display:flex;gap:32px;font-weight:700;font-size:15px}
.main-nav .active{position:relative}
.main-nav .active::after{content:"";position:absolute;left:0;right:0;bottom:-7px;height:3px;background:var(--red)}
.btn-login{position:absolute;left:960px;top:26px;width:95px;height:36px;border-radius:18px;background:var(--red);color:#fff;font-weight:700;font-size:15px;display:flex;align-items:center;justify-content:center;gap:5px}

/* hero */
.hero{position:absolute;left:0;top:85px;width:1200px;height:464px;background:linear-gradient(180deg,#b7b2aa 0%,#d99a6a 45%,#e2733f 62%,#4a3a40 85%,#1f2433 100%)}
.hero-title{position:absolute;left:0;width:1200px;top:180px;text-align:center;color:#fff;font-weight:900;font-size:56px;letter-spacing:1px}
.hero-sub{position:absolute;left:0;width:1200px;top:278px;text-align:center;color:#fff;font-size:28px;font-weight:400;text-shadow:0 1px 4px rgba(0,0,0,.4)}
.hero-by{position:absolute;left:0;width:1200px;top:242px;text-align:center;color:#fff;font-weight:900;font-size:24px;padding-left:150px}
.btn-start{position:absolute;left:505px;top:338px;width:190px;height:50px;border-radius:25px;background:var(--red);color:#fff;font-weight:700;font-size:16px;display:flex;align-items:center;justify-content:center;gap:6px}
.slider-dots{position:absolute;left:1136px;top:189px;display:flex;flex-direction:column;gap:8px}
.slider-dots span{width:11px;height:11px;border-radius:50%;background:#fff}
.slider-dots .on{background:transparent;border:2px solid #fff}

/* mosaic */
.tile{position:absolute;overflow:hidden}
.tile .shade{position:absolute;inset:0;background:linear-gradient(180deg,rgba(0,0,0,0) 45%,rgba(0,0,0,.6) 100%)}
.tile h3{position:absolute;left:25px;color:#fff;font-weight:700;font-size:20px;line-height:1.15}
.tile time{position:absolute;left:25px;color:var(--red);font-size:11px}
.tile.big h3{left:39px;font-size:27px;line-height:1.2}
.tile.big time{left:39px}

/* section */
.section-title{position:absolute;left:143px;font-weight:900;font-size:32px;letter-spacing:-.3px}
.feature-card{position:absolute;left:144px;width:274px;height:355px;background:#fff;box-shadow:0 1px 6px rgba(0,0,0,.12)}
.feature-card .photo{height:175px}
.feature-card .avatar{position:absolute;left:24px;top:202px;width:25px;height:25px;border-radius:50%;background:#8a7a70}
.feature-card h4{position:absolute;left:63px;top:197px;width:200px;font-size:18.5px;font-weight:400;line-height:1.18}
.feature-card p{position:absolute;left:24px;top:254px;width:235px;font-size:12.5px;color:var(--muted);line-height:1.5}
.feature-card hr{position:absolute;left:17px;right:17px;top:306px;border:0;border-top:1px solid var(--line)}
.meta{position:absolute;left:24px;top:322px;font-size:12.5px;display:flex;align-items:center;gap:6px}
.mini-post{position:absolute;left:444px;width:320px;height:95px}
.mini-post .thumb{position:absolute;left:0;top:0;width:121px;height:95px}
.mini-post h5{position:absolute;left:136px;top:9px;width:180px;font-size:19px;font-weight:400;line-height:1.25}
.mini-post time{position:absolute;left:136px;top:69px;font-size:12px;color:var(--date);display:flex;align-items:center;gap:5px}
.view-more{position:absolute;left:444px;color:var(--red);font-weight:700;font-size:16px}
.share-bar{position:absolute;left:144px;width:613px;height:52px;border-top:1px solid var(--line);border-bottom:1px solid var(--line)}
.share-bar .label{position:absolute;left:21px;top:16px;font-size:17px;font-weight:700}
.share-dots{position:absolute;left:129px;top:12px;display:flex;gap:5px}
.share-dots span{width:27px;height:27px;border-radius:50%}
.btn-comment{position:absolute;left:446px;top:7px;width:143px;height:38px;border-radius:19px;background:var(--red);color:#fff;font-weight:700;font-size:15px;display:flex;align-items:center;justify-content:center;gap:6px}

/* sidebar */
.widget{position:absolute;left:785px;width:270px;background:#fff;box-shadow:0 1px 6px rgba(0,0,0,.12)}
.widget .head{position:absolute;left:7px;right:7px;top:8px;height:36px;background:var(--panel-head);border:1px solid #d8d8d8;text-align:center;font-weight:900;font-size:24px;line-height:34px}
.search-field{position:absolute;left:20px;top:66px;width:230px;height:40px;border:1px solid #cfcfcf;border-radius:20px;font-size:12px;color:#555;padding:12px 20px}
.search-field .go{position:absolute;right:6px;top:7px;width:26px;height:26px;border-radius:50%;background:var(--red);display:flex;align-items:center;justify-content:center}
.doc-list{position:absolute;left:40px;top:80px;list-style:none}
.doc-list li{height:32px;font-size:14.5px;color:#444;display:flex;align-items:center;gap:16px}
.btn-pdf{position:absolute;left:40px;top:279px;width:191px;height:41px;border-radius:21px;background:var(--blue);color:#fff;font-weight:700;font-size:15px;display:flex;align-items:center;justify-content:center;gap:7px}
.nl-text{position:absolute;left:0;width:270px;top:72px;text-align:center;font-size:14.5px}
.nl-input{position:absolute;left:23px;width:220px;height:37px;border:1px solid #e2e2e2;box-shadow:0 1px 3px rgba(0,0,0,.08);font-size:12px;color:#666;padding:11px 18px}
.btn-signup{position:absolute;left:23px;top:197px;width:220px;height:37px;background:var(--blue);color:#fff;font-weight:700;font-size:15px;text-align:center;line-height:37px}
.social-grid{position:absolute;left:29px;top:94px;display:grid;grid-template-columns:repeat(3,47px);gap:19px 19px}
.social-grid span{width:47px;height:47px;border-radius:50%}

/* footer */
.site-footer{position:absolute;left:0;top:2182px;width:1200px;height:227px;background:var(--blue);border-top:4px solid var(--red)}
.contact-item{position:absolute;top:41px;display:flex;align-items:center;gap:16px;color:#fff;font-size:13.5px;line-height:1.65}
.contact-item .ring{width:40px;height:40px;border-radius:50%;border:1px solid rgba(255,255,255,.8);display:flex;align-items:center;justify-content:center;flex:none}
.footer-nav{position:absolute;left:0;width:1200px;top:110px;display:flex;justify-content:center;gap:32px;color:#fff;font-weight:700;font-size:16px}
.footer-bottom{position:absolute;left:0;top:160px;width:1200px;height:63px;background:var(--blue-dark)}
.footer-bottom p{position:absolute;left:144px;top:24px;color:#fff;font-size:13px}
.footer-social{position:absolute;left:918px;top:16px;display:flex;gap:5px}
.footer-social span{width:30px;height:30px;border-radius:50%;border:1px solid #fff}
</style>
</head>
<body>

<header class="site-header">
  <div class="brand"><span class="dot"></span>T-TARIFFS <small>by VALMOND</small></div>
  <nav class="main-nav">
    <a class="active">HOME</a><a>ABOUT US</a><a>SERVICES</a><a>BLOG</a><a>CONTACT US</a>
  </nav>
  <a class="btn-login">
    <svg width="12" height="13" viewBox="0 0 12 13"><circle cx="6" cy="3.5" r="3" fill="#fff"/><path d="M0 13c0-4 2.5-6 6-6s6 2 6 6z" fill="#fff"/></svg>LOG IN
  </a>
</header>

<section class="hero" role="img" aria-label="Cargo plane flying over port cranes at sunset">
  <div class="hero-title">T-TARIFFS</div>
  <div class="hero-by">by VALMOND</div>
  <div class="hero-sub">Lorem ipsum dolor sit amet consectetur adipiscing</div>
  <a class="btn-start">GET STARTED
    <svg width="13" height="13" viewBox="0 0 13 13"><circle cx="6.5" cy="6.5" r="6.5" fill="#fff"/><path d="M4 6.5h5M7 4.3l2.2 2.2L7 8.7" stroke="#e84a1f" stroke-width="1.6" fill="none"/></svg>
  </a>
  <div class="slider-dots"><span></span><span></span><span class="on"></span><span></span><span></span></div>
</section>

<section aria-label="Featured news">
  <article class="tile big" style="left:13px;top:562px;width:605px;height:429px">
    <div class="abs" style="inset:0;background:linear-gradient(180deg,#2f5fb0 0%,#5877a8 40%,#7c7d8a 62%,#3b3f52 100%)" role="img" aria-label="Container ship at port with highway and plane at dusk"></div>
    <div class="shade"></div>
    <h3 style="top:268px">Lorem ipsum dolor sit amet<br>consectetur adipiscing<br>elit sed do eiusmo</h3>
    <time style="top:381px">5 September 2019</time>
  </article>
  <article class="tile" style="left:631px;top:562px;width:271px;height:207px">
    <div class="abs" style="inset:0;background:linear-gradient(160deg,#8a8476,#b59a6e 55%,#5b4d3c)" role="img" aria-label="Parcels in a warehouse with a tablet"></div>
    <div class="shade"></div>
    <h3 style="top:120px">Lorem ipsum dolor<br>consectetur</h3><time style="top:176px">5 September 2019</time>
  </article>
  <article class="tile" style="left:915px;top:562px;width:272px;height:207px">
    <div class="abs" style="inset:0;background:linear-gradient(150deg,#24364a,#2f4b55 50%,#7a4e38)" role="img" aria-label="Aerial view of a container ship"></div>
    <div class="shade"></div>
    <h3 style="top:120px">Lorem ipsum dolor<br>consectetur</h3><time style="top:176px">5 September 2019</time>
  </article>
  <article class="tile" style="left:631px;top:784px;width:271px;height:207px">
    <div class="abs" style="inset:0;background:linear-gradient(150deg,#3b4f7a,#a86a6a 55%,#4a3040)" role="img" aria-label="Forklift in a warehouse"></div>
    <div class="shade"></div>
    <h3 style="top:120px">Lorem ipsum dolor<br>consectetur</h3><time style="top:176px">5 September 2019</time>
  </article>
  <article class="tile" style="left:915px;top:784px;width:272px;height:207px">
    <div class="abs" style="inset:0;background:linear-gradient(150deg,#9a5a44,#b3b9c2 50%,#6d4a3a)" role="img" aria-label="Stacked containers with a plane overhead"></div>
    <div class="shade"></div>
    <h3 style="top:120px">Lorem ipsum dolor<br>consectetur</h3><time style="top:176px">5 September 2019</time>
  </article>
</section>

<!-- recent blogs -->
<h2 class="section-title" style="top:1040px">RECENT BLOGS</h2>
<article class="feature-card" style="top:1106px">
  <div class="photo" style="background:linear-gradient(160deg,#7d7a72,#b79b6b 55%,#c2542d)" role="img" aria-label="Stacked cardboard boxes on a pallet"></div>
  <span class="avatar" role="img" aria-label="Author avatar"></span>
  <h4>Lorem ipsum dolor sit amet conseactetur</h4>
  <p>Sed ut perspiciatis unde omnis iste natus error sit voluptatem accusantium</p>
  <hr>
  <div class="meta"><svg width="11" height="11" viewBox="0 0 11 11"><rect x=".5" y="1.5" width="10" height="9" fill="none" stroke="#e84a1f"/><path d="M.5 4h10" stroke="#e84a1f"/></svg>Aug 31,2019 &nbsp;&nbsp;|&nbsp;&nbsp; <svg width="12" height="10" viewBox="0 0 12 10"><ellipse cx="6" cy="4.5" rx="6" ry="4.2" fill="#1f97dd"/></svg> 1</div>
</article>
<article class="mini-post" style="top:1106px"><div class="thumb" style="background:linear-gradient(135deg,#2d3d5e,#7d95b5 60%,#c9a64a)" role="img" aria-label="Worker inspecting a container"></div><h5>Lorem ipsum dolor sit amet</h5><time><svg width="11" height="11" viewBox="0 0 11 11"><rect x=".5" y="1.5" width="10" height="9" fill="none" stroke="#2a8fd4"/><path d="M.5 4h10" stroke="#2a8fd4"/></svg>Aug 31,2019</time></article>
<article class="mini-post" style="top:1214px"><div class="thumb" style="background:linear-gradient(135deg,#7a8ea8,#e29a4e 55%,#5a2e2e)" role="img" aria-label="Container ship at sunset"></div><h5>Lorem ipsum dolor sit amet</h5><time><svg width="11" height="11" viewBox="0 0 11 11"><rect x=".5" y="1.5" width="10" height="9" fill="none" stroke="#2a8fd4"/><path d="M.5 4h10" stroke="#2a8fd4"/></svg>Aug 31,2019</time></article>
<article class="mini-post" style="top:1322px"><div class="thumb" style="background:linear-gradient(135deg,#e8e4dc,#c9a270 55%,#9a3a2a)" role="img" aria-label="Parcels on a conveyor"></div><h5>Lorem ipsum dolor sit amet</h5><time><svg width="11" height="11" viewBox="0 0 11 11"><rect x=".5" y="1.5" width="10" height="9" fill="none" stroke="#2a8fd4"/><path d="M.5 4h10" stroke="#2a8fd4"/></svg>Aug 31,2019</time></article>
<a class="view-more" style="top:1447px">VIEW MORE</a>
<div class="share-bar" style="top:1505px">
  <span class="label">SHARE ON</span>
  <div class="share-dots"><span style="background:#2f4f9a"></span><span style="background:#2aa7e8"></span><span style="background:#5a4a3e"></span></div>
  <a class="btn-comment">COMMENT <svg width="12" height="12" viewBox="0 0 13 13"><circle cx="6.5" cy="6.5" r="6.5" fill="#fff"/><path d="M4 6.5h5M7 4.3l2.2 2.2L7 8.7" stroke="#e84a1f" stroke-width="1.6" fill="none"/></svg></a>
</div>

<!-- popular posts -->
<h2 class="section-title" style="top:1593px">POPULAR&nbsp; POSTS</h2>
<article class="feature-card" style="top:1659px">
  <div class="photo" style="background:linear-gradient(180deg,#3b4d6e,#6a7a90 40%,#a37a4a 70%,#2b2a35)" role="img" aria-label="Port terminal lit up at night"></div>
  <span class="avatar" role="img" aria-label="Author avatar"></span>
  <h4>Lorem ipsum dolor sit amet conseactetur</h4>
  <p>Sed ut perspiciatis unde omnis iste natus error sit voluptatem accusantium</p>
  <hr>
  <div class="meta"><svg width="11" height="11" viewBox="0 0 11 11"><rect x=".5" y="1.5" width="10" height="9" fill="none" stroke="#e84a1f"/><path d="M.5 4h10" stroke="#e84a1f"/></svg>Aug 31,2019 &nbsp;&nbsp;|&nbsp;&nbsp; <svg width="12" height="10" viewBox="0 0 12 10"><ellipse cx="6" cy="4.5" rx="6" ry="4.2" fill="#1f97dd"/></svg> 1</div>
</article>
<article class="mini-post" style="top:1659px"><div class="thumb" style="background:linear-gradient(135deg,#4a3a30,#b5542e 55%,#3a3a3a)" role="img" aria-label="Warehouse worker in a hard hat"></div><h5>Lorem ipsum dolor sit amet</h5><time><svg width="11" height="11" viewBox="0 0 11 11"><rect x=".5" y="1.5" width="10" height="9" fill="none" stroke="#2a8fd4"/><path d="M.5 4h10" stroke="#2a8fd4"/></svg>Aug 31,2019</time></article>
<article class="mini-post" style="top:1767px"><div class="thumb" style="background:linear-gradient(180deg,#8a6a80,#c47a62 50%,#e2a04a)" role="img" aria-label="Plane over a highway bridge"></div><h5>Lorem ipsum dolor sit amet</h5><time><svg width="11" height="11" viewBox="0 0 11 11"><rect x=".5" y="1.5" width="10" height="9" fill="none" stroke="#2a8fd4"/><path d="M.5 4h10" stroke="#2a8fd4"/></svg>Aug 31,2019</time></article>
<article class="mini-post" style="top:1875px"><div class="thumb" style="background:linear-gradient(135deg,#5a6070,#a5aab4 50%,#4a5060)" role="img" aria-label="Warehouse aisle with shelving"></div><h5>Lorem ipsum dolor sit amet</h5><time><svg width="11" height="11" viewBox="0 0 11 11"><rect x=".5" y="1.5" width="10" height="9" fill="none" stroke="#2a8fd4"/><path d="M.5 4h10" stroke="#2a8fd4"/></svg>Aug 31,2019</time></article>
<a class="view-more" style="top:2000px">VIEW MORE</a>
<div class="share-bar" style="top:2058px">
  <span class="label">SHARE ON</span>
  <div class="share-dots"><span style="background:#2f4f9a"></span><span style="background:#2aa7e8"></span><span style="background:#5a4a3e"></span></div>
  <a class="btn-comment">COMMENT <svg width="12" height="12" viewBox="0 0 13 13"><circle cx="6.5" cy="6.5" r="6.5" fill="#fff"/><path d="M4 6.5h5M7 4.3l2.2 2.2L7 8.7" stroke="#e84a1f" stroke-width="1.6" fill="none"/></svg></a>
</div>

<!-- sidebar -->
<aside>
  <section class="widget" style="top:1047px;height:128px">
    <div class="head">SEARCH</div>
    <div class="search-field">Search..
      <span class="go"><svg width="12" height="12" viewBox="0 0 12 12"><circle cx="5" cy="5" r="3.6" stroke="#fff" stroke-width="1.8" fill="none"/><path d="M7.6 7.6L10.5 10.5" stroke="#fff" stroke-width="1.8"/></svg></span>
    </div>
  </section>
  <section class="widget" style="top:1199px;height:356px">
    <div class="head" style="height:44px;line-height:42px">DOCUMENTS</div>
    <ul class="doc-list">
      <li><svg width="9" height="9" viewBox="0 0 9 9"><path d="M1 1l3 3.5L1 8M4.5 1l3 3.5-3 3.5" stroke="#e84a1f" stroke-width="1.3" fill="none"/></svg>Lorem ipsum dolo sit amet</li>
      <li><svg width="9" height="9" viewBox="0 0 9 9"><path d="M1 1l3 3.5L1 8M4.5 1l3 3.5-3 3.5" stroke="#e84a1f" stroke-width="1.3" fill="none"/></svg>At vero eos et accusamus</li>
      <li><svg width="9" height="9" viewBox="0 0 9 9"><path d="M1 1l3 3.5L1 8M4.5 1l3 3.5-3 3.5" stroke="#e84a1f" stroke-width="1.3" fill="none"/></svg>Eet iusto odio dignissimos</li>
      <li><svg width="9" height="9" viewBox="0 0 9 9"><path d="M1 1l3 3.5L1 8M4.5 1l3 3.5-3 3.5" stroke="#e84a1f" stroke-width="1.3" fill="none"/></svg>Ducimus qui blanditiis</li>
      <li><svg width="9" height="9" viewBox="0 0 9 9"><path d="M1 1l3 3.5L1 8M4.5 1l3 3.5-3 3.5" stroke="#e84a1f" stroke-width="1.3" fill="none"/></svg>praesentium voluptatum</li>
      <li><svg width="9" height="9" viewBox="0 0 9 9"><path d="M1 1l3 3.5L1 8M4.5 1l3 3.5-3 3.5" stroke="#e84a1f" stroke-width="1.3" fill="none"/></svg>Deleniti atque</li>
    </ul>
    <a class="btn-pdf">DOWNLOAD PDF <svg width="13" height="12" viewBox="0 0 13 12"><path d="M6.5 0v7M3.5 4.5l3 3 3-3" stroke="#fff" stroke-width="1.8" fill="none"/><rect x="0.5" y="9" width="12" height="3" fill="#fff"/></svg></a>
  </section>
  <section class="widget" style="top:1579px;height:253px">
    <div class="head" style="height:44px;line-height:42px">NEWSLETTER</div>
    <p class="nl-text">Lorem ipsum dolo sit amet</p>
    <div class="nl-input" style="top:96px">Enter Name</div>
    <div class="nl-input" style="top:147px">Enter Email</div>
    <a class="btn-signup">SIGN UP</a>
  </section>
  <section class="widget" style="top:1858px;height:250px;box-shadow:none;border:1px solid #e2e2e2">
    <div class="head" style="top:17px;height:44px;line-height:42px">SOCIAL MEDIA</div>
    <div class="social-grid">
      <span style="background:#3b5a9a"></span><span style="background:#2e2e2e"></span><span style="background:#c8232c"></span>
      <span style="background:#8cc63f"></span><span style="background:#1c6f9f"></span><span style="background:#2aa7e8"></span>
    </div>
  </section>
</aside>

<footer class="site-footer">
  <div class="contact-item" style="left:240px">
    <span class="ring"><svg width="12" height="16" viewBox="0 0 12 16"><path d="M6 0a6 6 0 0 0-6 6c0 4.5 6 10 6 10s6-5.5 6-10a6 6 0 0 0-6-6z" fill="#fff"/><circle cx="6" cy="6" r="2.2" fill="#1f97dd"/></svg></span>
    <span>314,At vero eos et accu<br>samus et iusto odio dimos ducimu</span>
  </div>
  <div class="contact-item" style="left:547px">
    <span class="ring"><svg width="15" height="15" viewBox="0 0 15 15"><path d="M3 0.5l3 3-1.7 2a9 9 0 0 0 5 5l2-1.7 3 3-2 2.5C6 14 1 9 0.5 2.5z" fill="#fff"/></svg></span>
    <span>1 800 555 0142</span>
  </div>
  <div class="contact-item" style="left:730px">
    <span class="ring"><svg width="17" height="12" viewBox="0 0 17 12"><rect width="17" height="12" rx="1.5" fill="#fff"/><path d="M1 1l7.5 6L16 1" stroke="#1f97dd" stroke-width="1.4" fill="none"/></svg></span>
    <span>info@ttariffs-valmond.com</span>
  </div>
  <nav class="footer-nav"><a>HOME</a><a>ABOUT US</a><a>SERVICES</a><a>BLOG</a><a>CONTACT US</a></nav>
  <div class="footer-bottom">
    <p>Copyrights © 2019, Ttariffs-valmond.All rights reserved.</p>
    <div class="footer-social"><span></span><span></span><span></span><span></span></div>
  </div>
</footer>

</body>
</html>
```